'Morrow Crest' wine label

We are looking to create a new wine brand called "Morrow Crest."

We have no preconceived notions about color, design or otherwise. This design should be incorporated into a wine label that will ultimately be affixed to either a 750ml bottle or a wine box. We've attached some images of wine label artwork and bottle shots - but yours does NOT need to look like these - they're there just for illustration purposes.

Target Market(s)

Target market for this wine brand will be "broad market" retail - i.e., big box stores, wine shops, etc.

Logo Text

Morrow Crest

```html
<!DOCTYPE html>
<html lang="en">
<head>
<meta charset="utf-8">
<title>Morrow Crest Cabernet Label</title>
<link href="https://fonts.googleapis.com/css2?family=Cinzel:wght@700&family=Arimo&family=Pinyon+Script&display=swap" rel="stylesheet">
<style>
  :root {
    --paper: #ffffff;
    --label-black: #000000;
    --sage: #9a9c88;
    --band-dark: #141414;
    --band-mid: #2c2c2a;
  }
  html, body {
    margin: 0;
    padding: 0;
    width: 1200px;
    height: 1200px;
    overflow: hidden;
    background: var(--paper);
  }
  .canvas {
    position: relative;
    width: 1200px;
    height: 1200px;
  }
  .label-frame {
    position: absolute;
    left: 427px;
    top: 243px;
    width: 346px;
    height: 873px;
    box-sizing: border-box;
    border: 3px solid var(--sage);
    background: var(--paper);
  }
  .label-body {
    position: absolute;
    left: 438px;
    top: 255px;
    width: 324px;
    height: 850px;
    background: var(--label-black);
  }
  .crest-artwork {
    position: absolute;
    left: 438px;
    top: 97px;
    width: 324px;
    height: 158px;
    background: linear-gradient(180deg, #1a1a1a 0%, var(--label-black) 100%);
  }
  .rule {
    position: absolute;
    height: 2px;
    background: var(--sage);
  }
  .rule--band-top { left: 438px; width: 324px; top: 396px; }
  .rule--band-bottom { left: 438px; width: 324px; top: 520px; }
  .rule--vintage { left: 492px; width: 215px; top: 1009px; }
  .lattice-band {
    position: absolute;
    left: 438px;
    width: 324px;
    top: 399px;
    height: 120px;
    background: linear-gradient(180deg, var(--band-dark) 0%, var(--band-mid) 50%, var(--band-dark) 100%);
  }
  .brand-name {
    position: absolute;
    left: 438px;
    width: 324px;
    top: 336px;
    margin: 0;
    text-align: center;
    font-family: "Cinzel", serif;
    font-weight: 700;
    font-size: 28px;
    letter-spacing: 1px;
    color: var(--sage);
    line-height: 1;
  }
  .varietal {
    position: absolute;
    left: 438px;
    width: 324px;
    top: 543px;
    margin: 0;
    text-align: center;
    font-family: "Arimo", sans-serif;
    font-size: 26px;
    letter-spacing: 12px;
    padding-left: 12px;
    box-sizing: border-box;
    color: var(--sage);
    line-height: 1;
  }
  .vintage {
    position: absolute;
    left: 438px;
    width: 324px;
    top: 955px;
    margin: 0;
    text-align: center;
    font-family: "Arimo", sans-serif;
    font-size: 31px;
    letter-spacing: 8px;
    padding-left: 8px;
    box-sizing: border-box;
    color: var(--sage);
    line-height: 1;
  }
  .region {
    position: absolute;
    left: 438px;
    width: 324px;
    top: 1030px;
    margin: 0;
    text-align: center;
    font-family: "Pinyon Script", cursive;
    font-size: 40px;
    color: var(--sage);
    line-height: 1.2;
  }
</style>
</head>
<body>
<div class="canvas">
  <div class="label-frame"></div>
  <div class="crest-artwork" role="img" aria-label="Mountain peak silhouette forming the top of the label"></div>
  <div class="label-body"></div>

  <h1 class="brand-name">Morrow Crest</h1>
  <div class="rule rule--band-top"></div>
  <div class="lattice-band" role="img" aria-label="Decorative dark lattice pattern band"></div>
  <div class="rule rule--band-bottom"></div>
  <p class="varietal">CABERNET</p>
  <p class="vintage">2003</p>
  <div class="rule rule--vintage"></div>
  <p class="region">Napa Valley</p>
</div>
</body>
</html>
```